Flyer Design Project

We want to design a flyer to distribute locally to advise the community that we are a brand new medical centre that has opened in the heart of Parramatta!

Target Market(s)

More so corporate clients but also family friendly

Industry/Entity Type

Medical

Requirements
Must have
• Try stick to blue theme if possible but compliment with another colour.
Brand new medical centre that has opened in the heart of Parramatta!
A5 size flyer.
Corporate & modern feel.
Small box that shows our map location with nearby train station, parking & street location.
We bulk bill.
Appointments and walk-ins are welcome!
Open 6 days.

```html
<!DOCTYPE html>
<html lang="en">
<head>
<meta charset="utf-8">
<title>Harbourline Health Clinic – Flyer</title>
<link rel="stylesheet" href="https://fonts.googleapis.com/css2?family=Varela+Round&family=Oswald:wght@500&display=swap">
<style>
  :root {
    --canvas: #ffffff;
    --sky: #1b9be0;
    --sky-deep: #0c78c4;
    --sky-light: #5fc0f2;
    --navy: #2b3a6b;
    --navy-deep: #1f2c59;
    --ink: #ffffff;
    --grey: #b5b5b5;
    --frame: #2a2a2a;
  }
  * { box-sizing: border-box; margin: 0; padding: 0; }
  html, body { width: 1200px; height: 854px; overflow: hidden; background: var(--canvas); }
  body { position: relative; font-family: "Varela Round", "Helvetica Neue", sans-serif; color: var(--ink); }

  .page { position: absolute; top: 18px; width: 577px; height: 818px; overflow: hidden; }
  .page--front { left: 18px; background: linear-gradient(180deg, #2a8fd6 0%, var(--sky) 45%, #3aa6e6 100%); }
  .page--back { left: 605px; background: var(--navy); }

  .photo { position: absolute; }
  .photo--drinkers { left: 300px; top: 0; width: 277px; height: 230px;
    background: linear-gradient(135deg, #cfe6f5 0%, #8fc3e4 50%, #3f92cf 100%); }
  .photo--doctor { left: 170px; top: 430px; width: 407px; height: 331px;
    background: radial-gradient(ellipse at 65% 60%, #f2f7fb 0%, #c7def0 35%, #5aa9de 75%, rgba(27,155,224,0) 100%); }

  .wave { position: absolute; left: 0; top: 0; }

  .brand { position: absolute; left: 96px; top: 71px; width: 164px; height: 164px; border: 2px solid #bfe3f7; border-radius: 50%;
    display: flex; align-items: center; justify-content: center; text-align: center;
    color: #8a9bb0; font-size: 17px; letter-spacing: 3px; line-height: 1.35; }

  .intro { position: absolute; right: 39px; top: 313px; text-align: right; font-size: 16.5px; line-height: 21px; }
  .intro p + p { margin-top: 21px; }

  .contact { position: absolute; right: 39px; top: 470px; text-align: right; font-size: 13px; line-height: 14.3px; }
  .contact strong { font-weight: 700; }

  .badge { position: absolute; left: 0; top: 481px; width: 142px; height: 123px; }
  .badge-text { position: absolute; left: 0; top: 481px; width: 120px; height: 123px;
    font-family: "Oswald", "Arial Narrow", sans-serif; font-weight: 500; text-align: center; line-height: 1; color: var(--ink); }
  .badge-text span { display: block; }
  .badge-text .b-open { font-size: 26px; margin-top: 13px; }
  .badge-text .b-num { font-size: 40px; }
  .badge-text .b-days { font-size: 26px; }

  .billing { position: absolute; left: 43px; top: 666px; font-size: 16px; line-height: 21px; }

  .hours { position: absolute; left: 0; bottom: 0; width: 100%; height: 58px; background: var(--navy-deep);
    text-align: center; padding-top: 8px; }
  .hours h2 { font-size: 14px; font-weight: 400; letter-spacing: .3px; line-height: 16px; }
  .hours p { font-size: 11px; line-height: 12.5px; font-weight: 700; }

  .tab { position: absolute; left: 53px; top: 0; width: 472px; height: 54px; border-radius: 0 0 10px 10px;
    background: linear-gradient(180deg, var(--sky-deep), var(--sky) 60%, var(--sky-light));
    display: flex; align-items: center; justify-content: center; font-size: 15.5px; font-weight: 700; letter-spacing: .3px; }

  .welcome { position: absolute; left: 30px; top: 84px; width: 517px; text-align: center; font-size: 11px; line-height: 14px; }
  .welcome p + p { margin-top: 14px; }

  .card { position: absolute; top: 254px; width: 237px; height: 293px; border-radius: 10px; overflow: hidden; background: var(--sky); }
  .card--scope { left: 26px; }
  .card--values { left: 314px; }
  .card-body { height: 176px; padding: 30px 18px 0 22px; font-size: 10.5px; line-height: 11.3px; }
  .card-body ul { list-style: none; margin-top: 13px; }
  .card-body li { position: relative; padding-left: 11px; }
  .card-body li::before { content: "•"; position: absolute; left: 0; }
  .card-photo { height: 117px; }
  .card-photo--stress { background: linear-gradient(135deg, #6b4a33, #c48d68 55%, #e3b38f); }
  .card-photo--consult { background: linear-gradient(135deg, #dfe9f1, #b7c7d4 50%, #8b9cab); }

  .glow { position: absolute; left: 0; top: 582px; width: 100%; height: 28px;
    background: radial-gradient(ellipse at 50% 100%, var(--sky-light) 0%, var(--sky-deep) 40%, rgba(43,58,107,0) 75%); }
  .footer { position: absolute; left: 0; top: 610px; width: 100%; height: 208px; background: var(--grey); }
  .map { position: absolute; left: 133px; top: 11px; width: 312px; height: 182px; border: 4px solid var(--frame);
    background: linear-gradient(135deg, #e9e4d4 0%, #f1efe5 40%, #d9e8c4 70%, #b8d4e8 100%); }
</style>
</head>
<body>

<section class="page page--front">
  <div class="photo photo--drinkers" role="img" aria-label="Photo of two active adults drinking bottled water outdoors"></div>
  <div class="photo photo--doctor" role="img" aria-label="Photo of a doctor in a white coat with a stethoscope"></div>

  <svg class="wave" width="577" height="420" viewBox="0 0 577 420" aria-hidden="true">
    <defs>
      <linearGradient id="edge" x1="0" y1="0" x2="1" y2="1">
        <stop offset="0" stop-color="#1f2c59"/>
        <stop offset="1" stop-color="#1b7fc9"/>
      </linearGradient>
    </defs>
    <path d="M0 0 H306 C250 70 300 190 470 238 C300 262 130 320 0 392 Z" fill="url(#edge)"/>
    <path d="M0 0 H290 C236 70 280 185 440 228 C280 252 120 300 0 370 Z" fill="#ffffff"/>
  </svg>

  <div class="brand">Harbourline<br>Health</div>

  <div class="intro">
    <p>Harbourline Health Clinic<br>is a general practice catering for the working<br>community of Parramatta and its surrounding suburbs.</p>
    <p>It strives to achieve a collaborative approach<br>in healthcare by its emphasis, although not exclusive,<br>in preventive medical management.</p>
  </div>

  <div class="contact">
    <strong>Harbourline Health Clinic</strong><br>
    18 Kestrel Street, Parramatta NSW 2150<br>
    Phone: 02 5550 0147<br>
    Fax: 02 5550 0148
  </div>

  <svg class="badge" viewBox="0 0 142 123" aria-hidden="true">
    <defs>
      <linearGradient id="badgeFill" x1="0" y1="0" x2="1" y2="0">
        <stop offset="0" stop-color="#1f3f84"/>
        <stop offset="1" stop-color="#1689d6"/>
      </linearGradient>
    </defs>
    <path d="M0 0 H120 L142 61.5 L120 123 H0 Z" fill="url(#badgeFill)"/>
  </svg>
  <div class="badge-text"><span class="b-open">OPEN</span><span class="b-num">6</span><span class="b-days">DAYS</span></div>

  <p class="billing">Bulk billing is at the discretion<br>of the doctor in discussion<br>with individual patients.</p>

  <footer class="hours">
    <h2>OPENING HOURS</h2>
    <p>Monday – Friday (8:00am – 6:00pm) | Saturday (8:00am – 1:00pm)<br>Sunday &amp; Public Holidays Closed</p>
  </footer>
</section>

<section class="page page--back">
  <h1 class="tab">APPOINTMENTS AND WALK-INS ARE WELCOME!</h1>

  <div class="welcome">
    <p>Harbourline Health Clinic is primarily run on bookings and we strive hard to accommodate<br>patients on time. Our appointments are booked at 20 minute increments.</p>
    <p>Please inform the receptionist beforehand if you require longer consultations.<br>Consultations requiring long appointments include pap smears, travel vaccinations, health checks<br>and work-related cases.</p>
    <p>In an emergency, we may need to spend extra time with you to ensure you are safe and cared for.<br>Thus, we appreciate your patience if our doctors are occasionally running late.</p>
  </div>

  <article class="card card--scope">
    <div class="card-body">
      <p>Our scope of practice emphasises on,<br>but is not limited to the following:</p>
      <ul>
        <li>Men's Health</li>
        <li>Women's Health</li>
        <li>Skin Health</li>
        <li>Injury Diagnosis &amp; Management</li>
        <li>Adult Medicine Preventative Health Assessment</li>
        <li>Travel Medicine &amp; Vaccinations</li>
      </ul>
    </div>
    <div class="card-photo card-photo--stress" role="img" aria-label="Photo of a man holding his head in his hands"></div>
  </article>

  <article class="card card--values">
    <div class="card-body">
      <p>Our values show who we are and<br>what we do:</p>
      <ul>
        <li>We always act responsibly &amp; ethically</li>
        <li>We aim to be distinct &amp; different</li>
        <li>We strongly believe in a team approach to medical management</li>
        <li>We strive to be relevant &amp; practical</li>
      </ul>
    </div>
    <div class="card-photo card-photo--consult" role="img" aria-label="Photo of a doctor listening to an older patient with a stethoscope"></div>
  </article>

  <div class="glow"></div>
  <div class="footer">
    <div class="map" role="img" aria-label="Street map of central Parramatta showing the clinic location, nearby train station and parking"></div>
  </div>
</section>

</body>
</html>
```